Stride Collective_NTR Brand Set Up

We need the following for a new sports academy based in Cairns, QLD Australia called Stride Collective_NTR:<br/>Digital design medium for:<br/>Business identity logo / designs<br/>Header<br/>Email signature block<br/>Website with bookings & payments <br/>Social media - Instagram, Facebook<br/><br/>Colours based on Fluoro green, black & white greys

Target Market(s)

Sports

Colors

Designer to choose colors to be used in the design.

Requirements
Must have
• Sharp professional look

```html
<!DOCTYPE html>
<html lang="en">
<head>
<meta charset="utf-8">
<title>Stride Collective_NTR – Junior Development Flyer</title>
<link rel="stylesheet" href="https://fonts.googleapis.com/css2?family=Rajdhani:wght@500;600;700&display=swap">
<style>
  :root {
    --fluoro: #17b523;
    --fluoro-dark: #0f8f1a;
    --black: #000000;
    --ghost: #161616;
    --white: #ffffff;
    --stands: #3d4a34;
    --stands-light: #7c8a6e;
    --pitch-bright: #6fb23a;
    --pitch-mid: #4f9428;
    --pitch-dark: #24511a;
    --kit-teal: #2f9a6a;
    --gold: #c9b26a;
  }
  * { margin: 0; padding: 0; box-sizing: border-box; }
  html, body { width: 1063px; height: 1200px; overflow: hidden; background: var(--black); }
  body { font-family: "Rajdhani", "Arial Narrow", sans-serif; color: var(--white); }

  .flyer { position: relative; width: 1063px; height: 1200px; background: var(--black); overflow: hidden; }

  .hero-photo {
    position: absolute; left: 0; top: 0; width: 1063px; height: 650px;
    background:
      radial-gradient(ellipse 180px 300px at 610px 300px, rgba(47,154,106,0.55) 0%, rgba(47,154,106,0) 100%),
      radial-gradient(ellipse 420px 180px at 560px 430px, rgba(140,200,80,0.35) 0%, rgba(140,200,80,0) 100%),
      linear-gradient(180deg,
        var(--stands) 0%,
        var(--stands-light) 18%,
        #5a7a43 32%,
        var(--pitch-bright) 42%,
        var(--pitch-mid) 68%,
        var(--pitch-dark) 100%);
  }
  .hero-shapes { position: absolute; left: 0; top: 0; width: 1063px; height: 650px; }

  .brand-mark {
    position: absolute; left: 22px; top: 38px;
    font-weight: 700; font-size: 86px; letter-spacing: 5px; line-height: 1;
    color: var(--fluoro);
  }

  .tagline {
    position: absolute; left: 36px; top: 666px;
    font-weight: 700; font-size: 22px; letter-spacing: 0.3px; text-transform: uppercase;
  }

  .headline { position: absolute; left: 34px; top: 692px; line-height: 0.9; }
  .headline-line { display: block; font-weight: 700; font-size: 84px; letter-spacing: 1px; color: var(--fluoro); text-transform: uppercase; }
  .headline-ghost { position: absolute; left: 50px; top: 722px; line-height: 0.9; }
  .headline-ghost .headline-line { color: var(--ghost); font-size: 90px; }

  .headline-rule { position: absolute; left: 36px; top: 858px; width: 490px; height: 5px; background: var(--white); }

  .cta-banner { position: absolute; left: 36px; top: 876px; width: 880px; height: 66px; }
  .cta-text {
    position: absolute; left: 116px; top: 880px;
    font-weight: 700; font-size: 48px; letter-spacing: 1.6px; color: var(--fluoro); text-transform: uppercase;
  }

  .age-line { position: absolute; left: 38px; top: 964px; font-weight: 500; font-size: 54px; letter-spacing: 1.5px; }
  .age-line strong { font-weight: 700; }

  .contact-row { position: absolute; left: 38px; top: 1046px; display: flex; align-items: center; font-weight: 500; font-size: 48px; letter-spacing: 1.2px; line-height: 1; }
  .contact-item { display: flex; align-items: center; gap: 20px; }
  .contact-item + .contact-item { margin-left: 54px; }
  .contact-icon { width: 46px; height: 46px; display: block; }

  .footer-rule { position: absolute; left: 0; top: 1102px; width: 1063px; height: 7px; background: var(--fluoro); }
  .footer {
    position: absolute; left: 0; top: 1109px; width: 1063px; height: 91px; background: var(--white);
    display: flex; align-items: center; justify-content: center; gap: 18px;
  }
  .web-address { font-weight: 700; font-size: 56px; letter-spacing: 1px; color: var(--fluoro); text-transform: uppercase; }
  .globe-icon { width: 40px; height: 40px; }
</style>
</head>
<body>
<main class="flyer">

  <div class="hero-photo" role="img" aria-label="Photo of a young player in a green kit kicking a ball on a grass training field"></div>

  <svg class="hero-shapes" viewBox="0 0 1063 650" aria-hidden="true">
    <defs>
      <linearGradient id="goldStripe" x1="0" y1="1" x2="1" y2="0">
        <stop offset="0" stop-color="#1a1a1a"/>
        <stop offset="0.35" stop-color="var(--gold)"/>
        <stop offset="1" stop-color="#1a1a1a" stop-opacity="0"/>
      </linearGradient>
    </defs>
    <polygon points="0,0 560,0 0,290" fill="var(--black)"/>
    <polygon points="0,290 560,0 590,0 0,308" fill="url(#goldStripe)"/>
    <polygon points="0,308 590,0 600,0 0,314" fill="var(--black)"/>
    <polygon points="720,235 1063,60 1063,70 735,235" fill="var(--black)"/>
    <polygon points="780,240 1063,90 1063,96 792,240" fill="var(--black)"/>
    <polygon points="1063,440 1063,650 560,650" fill="var(--black)"/>
    <polygon points="470,650 1063,385 1063,425 520,650" fill="var(--fluoro)"/>
    <polygon points="545,650 1063,445 1063,498 620,650" fill="var(--fluoro)"/>
    <polygon points="640,650 1063,510 1063,518 660,650" fill="var(--fluoro-dark)"/>
    <rect x="0" y="628" width="510" height="14" fill="var(--fluoro)"/>
    <rect x="0" y="642" width="1063" height="8" fill="var(--black)"/>
  </svg>

  <div class="brand-mark">SC_NTR</div>

  <p class="tagline">Australian Rules Football Junior Development Private Coaching</p>

  <div class="headline-ghost" aria-hidden="true">
    <span class="headline-line">Stride</span>
    <span class="headline-line">Collective_NTR</span>
  </div>
  <h1 class="headline">
    <span class="headline-line">Stride</span>
    <span class="headline-line">Collective_NTR</span>
  </h1>

  <div class="headline-rule"></div>

  <svg class="cta-banner" viewBox="0 0 880 66" aria-hidden="true">
    <polygon points="50,8 880,8 830,66 0,66" fill="var(--fluoro)"/>
    <polygon points="50,0 866,0 816,58 0,58" fill="var(--white)"/>
  </svg>
  <p class="cta-text">Register your interest today</p>

  <p class="age-line">AGE <strong>6 - 16</strong> ( BOYS &amp; GIRLS )</p>

  <div class="contact-row">
    <div class="contact-item">
      <svg class="contact-icon" viewBox="0 0 44 44" aria-hidden="true">
        <rect x="4" y="4" width="40" height="40" fill="var(--fluoro)"/>
        <rect x="0" y="0" width="40" height="40" fill="var(--white)"/>
        <path d="M11 8c2 0 5 6 5 7.5s-3 2.5-2.5 4c1 3 4 6 7 7 1.5.5 2.5-2.5 4-2.5S32 27 32 29c0 2.5-3 4-5 4-9 0-18-9-18-18 0-2 1.5-7 2-7z" fill="var(--fluoro)"/>
      </svg>
      <span>0400 217 604</span>
    </div>
    <div class="contact-item">
      <svg class="contact-icon" viewBox="0 0 44 44" aria-hidden="true">
        <rect x="4" y="4" width="40" height="40" fill="var(--fluoro)"/>
        <rect x="0" y="0" width="40" height="40" fill="var(--white)"/>
        <rect x="6" y="11" width="28" height="19" fill="var(--fluoro)"/>
        <path d="M7 12l13 10 13-10" fill="none" stroke="var(--white)" stroke-width="2.5"/>
      </svg>
      <span>HELLO@STRIDENTR.COM.AU</span>
    </div>
  </div>

  <div class="footer-rule"></div>
  <footer class="footer">
    <svg class="globe-icon" viewBox="0 0 38 38" aria-hidden="true">
      <circle cx="19" cy="19" r="17" fill="none" stroke="var(--fluoro)" stroke-width="3"/>
      <ellipse cx="19" cy="19" rx="7" ry="17" fill="none" stroke="var(--fluoro)" stroke-width="2.5"/>
      <line x1="2" y1="19" x2="36" y2="19" stroke="var(--fluoro)" stroke-width="2.5"/>
      <line x1="5" y1="11" x2="33" y2="11" stroke="var(--fluoro)" stroke-width="2"/>
      <line x1="5" y1="27" x2="33" y2="27" stroke="var(--fluoro)" stroke-width="2"/>
    </svg>
    <span class="web-address">www.stridentr.com.au</span>
  </footer>

</main>
</body>
</html>
```